Residential Construction Business - Site Signage

I need a design made for a site fence banner. We have a logo and branding so the design would need to be aligned with this. It would need to be made to specific size ratio so that it can be sent to the maker for production.
ratio : 4600 wide x 1700 high
The design should feature our website and also the slogan
"don't move, re-imagine"

Target Market(s)

potential clients

Industry/Entity Type

construction

Font styles to use
Other font styles liked:
• to match branding

Colors
0054AA
0677BA
7BADD7
CADEEF
E8F1F8

Requirements
Must have
• www.velmbuild.com.au Majority of the sign is our brand logo
Nice to have
• Majority of the sign is our brand logo
Should not have
• colors and themes that arent brand relevant

```html
<!DOCTYPE html>
<html lang="en">
<head>
<meta charset="utf-8">
<title>Velm Build – Site Fence Banner</title>
<link rel="stylesheet" href="https://fonts.googleapis.com/css2?family=Montserrat:wght@400;600;700&display=swap">
<style>
  :root {
    --brand-navy: #0054AA;
    --brand-blue: #0677BA;
    --brand-sky: #7BADD7;
    --brand-mist: #CADEEF;
    --brand-ice: #E8F1F8;
    --photo-deep: #0F4A72;
    --photo-mid: #2F6690;
    --band-blue: #3F82CC;
    --band-light: #A9D2E8;
    --panel-pale: #F1F8FB;
    --white: #FFFFFF;
  }
  html, body {
    margin: 0;
    padding: 0;
    overflow: hidden;
    background: var(--white);
  }
  .banner {
    position: relative;
    width: 1200px;
    height: 443px;
    overflow: hidden;
    font-family: "Montserrat", sans-serif;
  }
  .banner__art {
    position: absolute;
    inset: 0;
    width: 1200px;
    height: 443px;
    display: block;
  }
  .wordmark {
    position: absolute;
    left: 93px;
    top: 205px;
    margin: 0;
    font-size: 29px;
    font-weight: 600;
    letter-spacing: 0.36em;
    line-height: 1;
    color: var(--white);
    white-space: nowrap;
  }
  .slogan {
    position: absolute;
    left: 655px;
    top: 86px;
    margin: 0;
    font-size: 41px;
    font-weight: 400;
    line-height: 1;
    color: var(--brand-navy);
    white-space: nowrap;
    letter-spacing: 0.005em;
  }
  .slogan strong { font-weight: 700; }
  .website {
    position: absolute;
    left: 655px;
    top: 314px;
    margin: 0;
    font-size: 37px;
    font-weight: 400;
    line-height: 1;
    color: var(--brand-navy);
    white-space: nowrap;
  }
  .website strong { font-weight: 700; }
</style>
</head>
<body>
<main class="banner">
  <svg class="banner__art" viewBox="0 0 1200 443" xmlns="http://www.w3.org/2000/svg" aria-hidden="false">
    <defs>
      <linearGradient id="site-photo-tone" x1="0" y1="0" x2="1" y2="1">
        <stop offset="0" stop-color="var(--photo-mid)"/>
        <stop offset="1" stop-color="var(--photo-deep)"/>
      </linearGradient>
      <linearGradient id="sign-photo-tone" x1="0" y1="0" x2="1" y2="0">
        <stop offset="0" stop-color="#D7E5F1"/>
        <stop offset="1" stop-color="#E4EEF5"/>
      </linearGradient>
    </defs>

    <rect class="site-photo" x="0" y="0" width="1200" height="443" fill="url(#site-photo-tone)"
          role="img" aria-label="Photo of a house under construction wrapped in scaffolding, tinted blue"/>

    <polygon class="sign-photo" points="708,0 1200,0 1200,221 524,221"
             fill="url(#sign-photo-tone)"
             role="img" aria-label="Faded photo of a company site sign on a fence"/>

    <polygon class="pale-panel" points="524,221 1200,221 1200,443 731,443" fill="var(--panel-pale)"/>

    <path class="chevron chevron--deep"
          d="M573,0 L398,205 Q388,219 398,233 L592,443 L661,443 L466,233 Q456,219 466,205 L643,0 Z"
          fill="var(--band-blue)" opacity="0.9"/>
    <path class="chevron chevron--light"
          d="M643,0 L466,205 Q456,219 466,233 L661,443 L731,443 L531,233 Q521,219 531,205 L708,0 Z"
          fill="var(--band-light)"/>
  </svg>

  <p class="wordmark">VELM BUILD</p>
  <h1 class="slogan">Don’t <strong>Move</strong>, Re-Imagine</h1>
  <p class="website">www.<strong>velm</strong>build.com.au</p>
</main>
</body>
</html>
```